Hello,
Marisol Trent Equestrian needs a business card. We are a high performance show jumping stables based at Oakhollow Paddocks in morningotn. We pride ourselves on producing high quality show jumping horses and competing our stock at a high level. My business card need to have my logo on it, and i would like it to have a classic design with a modern touch. I would like it to have quite a natural feel about it. It needs to be in a font which is easy to read as I spend a lot of time competing internationally and overseas, and i need to be able to give it out to breeders and contacts where English isnt their first language. I will need it to include the following details:
-Marisol Trent Equestrian
-Based at Oakhollow Paddocks Ashcombe Vale
-Address: 17 Pemberly Lane Ashcombe Vale Westmere 3990
-Mobile number: 0412659048
- website: www.marisoltrentequestrian-example.com
Target Market(s)
For business adults who english may not be their first language
Industry/Entity Type
Business

```html
<!DOCTYPE html>
<html lang="en">
<head>
<meta charset="utf-8">
<title>Marisol Trent Equestrian – Business Card</title>
<link rel="stylesheet" href="https://fonts.googleapis.com/css2?family=Cinzel:wght@400;500&family=Raleway:wght@300;400;600&display=swap">
<style>
  :root {
    --backdrop: #dcd7cf;
    --paper: #ecebe6;
    --bronze: #9b7435;
    --ink: #262626;
    --ink-soft: #6b6b6b;
    --mark-grey: #7a7672;
  }
  * { box-sizing: border-box; margin: 0; padding: 0; }
  html, body {
    width: 1200px;
    height: 1000px;
    overflow: hidden;
    background: var(--backdrop);
  }
  .canvas {
    width: 1200px;
    height: 1000px;
    display: flex;
    flex-direction: column;
    align-items: center;
    justify-content: center;
    gap: 36px;
  }
  .card {
    width: 760px;
    height: 434px;
    background: var(--paper);
    box-shadow: 0 2px 10px rgba(0,0,0,0.12);
    position: relative;
  }
  .card-back {
    display: flex;
    align-items: center;
    justify-content: center;
    gap: 18px;
  }
  .card-back .brand-name {
    font-family: "Cinzel", serif;
    font-weight: 400;
    font-size: 30px;
    letter-spacing: 1px;
    color: var(--bronze);
  }
  .card-back .brand-dot {
    width: 44px;
    height: 44px;
    border-radius: 50%;
    background: var(--bronze);
  }
  .card-front {
    padding: 70px 56px 0 62px;
  }
  .card-front .header {
    display: flex;
    align-items: flex-start;
    justify-content: space-between;
  }
  .card-front .brand-name {
    font-family: "Cinzel", serif;
    font-weight: 500;
    font-size: 36px;
    letter-spacing: 0.5px;
    color: var(--ink);
    line-height: 1.1;
  }
  .card-front .location {
    font-family: "Raleway", sans-serif;
    font-weight: 300;
    font-size: 25px;
    color: var(--ink-soft);
    margin-top: 2px;
  }
  .card-front .brand-dot {
    width: 70px;
    height: 70px;
    border-radius: 50%;
    background: var(--mark-grey);
    margin-top: 14px;
    flex-shrink: 0;
  }
  .contact-list {
    list-style: none;
    margin-top: 62px;
    font-family: "Raleway", sans-serif;
    font-size: 20px;
    line-height: 1.45;
    color: var(--ink);
  }
  .contact-list .label { font-weight: 600; }
  .contact-list .value { font-weight: 400; }
</style>
</head>
<body>
  <main class="canvas">
    <section class="card card-back" aria-label="Card back">
      <span class="brand-name">Marisol Trent Equestrian</span>
      <span class="brand-dot" aria-hidden="true"></span>
    </section>

    <section class="card card-front" aria-label="Card front">
      <div class="header">
        <div class="identity">
          <h1 class="brand-name">Marisol Trent Equestrian</h1>
          <p class="location">Oakhollow Paddocks Ashcombe Vale</p>
        </div>
        <span class="brand-dot" aria-hidden="true"></span>
      </div>
      <ul class="contact-list">
        <li><span class="label">Address:</span> <span class="value">17 Pemberly Lane Ashcombe Vale Westmere 3990</span></li>
        <li><span class="label">Mobile Number:</span> <span class="value">0412659048</span></li>
        <li><span class="label">Website:</span> <span class="value">www.marisoltrentequestrian-example.com</span></li>
      </ul>
    </section>
  </main>
</body>
</html>
```